Business Card Design To Look Just Like a Credit Card- Needed

I would like to take my new Logo just designed here at Pixel Harbor and make a new business card and template for future additional sales people.
The credit card should have an eye catching design but look real. I have seen some that have similar logos to LORU or TrustPlaque too. However,it must have a smart chip design in it too. Make sure it has a black fake magnetic strip and other characteristics of an actual modern credit card.
This may be printed on paper and blank plastic cards.

Most the information will be on the back but the name will be on front with the logo, phone number.

Must Have Info:
Leonard Whitfield
President

2964 Maple Hollow Rd, Bldg 417
Fairport, NY 14582
252-555-0187
leonard@brightledgerco.net
Updates

Phone number is 585 area code not 252! my bad

also, please add website address www.brightledgerco.net
Thanks,

LW

Industry/Entity Type

Credit Card

Requirements
Must have
• My Logo, smart chip, fake magnetic strip

```html
<!DOCTYPE html>
<html lang="en">
<head>
<meta charset="utf-8">
<title>Bright Ledger Co — Card Back</title>
<link rel="stylesheet" href="https://fonts.googleapis.com/css2?family=Arimo:wght@700&display=swap">
<style>
  :root {
    --card-yellow: #f4dc04;
    --ghost-yellow: #e6d300;
    --brand-green: #0f7a1c;
    --chip-grey: #4d4d4d;
    --stripe-black: #000000;
  }
  html, body {
    margin: 0;
    padding: 0;
    overflow: hidden;
  }
  .card {
    position: relative;
    width: 1200px;
    height: 724px;
    background: var(--card-yellow);
    overflow: hidden;
    font-family: "Arimo", Arial, sans-serif;
    font-weight: 700;
  }
  .ghost-name {
    position: absolute;
    left: 61px;
    top: 190px;
    margin: 0;
    color: var(--ghost-yellow);
    font-size: 170px;
    line-height: 160px;
    letter-spacing: -2px;
    white-space: nowrap;
  }
  .ghost-name span {
    display: block;
  }
  .ghost-name .line-two {
    padding-left: 120px;
  }
  .brand-name {
    position: absolute;
    margin: 0;
    color: var(--brand-green);
    letter-spacing: -1px;
    white-space: nowrap;
  }
  .brand-name span {
    display: block;
  }
  .brand-top {
    left: 488px;
    top: 149px;
    font-size: 50px;
    line-height: 41px;
  }
  .brand-top .line-two {
    padding-left: 37px;
  }
  .brand-bottom {
    left: 800px;
    top: 557px;
    font-size: 54px;
    line-height: 47px;
  }
  .brand-bottom .line-two {
    padding-left: 40px;
  }
  .chip {
    position: absolute;
    left: 56px;
    top: 279px;
  }
  .magnetic-stripe {
    position: absolute;
    left: 0;
    top: 500px;
    width: 1200px;
    height: 58px;
    background: var(--stripe-black);
  }
  .rule {
    position: absolute;
    left: 6px;
    top: 651px;
    width: 1194px;
    height: 3px;
    background: var(--brand-green);
  }
</style>
</head>
<body>
<div class="card">
  <p class="ghost-name" aria-hidden="true"><span>BRIGHT</span><span class="line-two">LEDGER CO</span></p>

  <h1 class="brand-name brand-top"><span>BRIGHT</span><span class="line-two">LEDGER CO</span></h1>

  <svg class="chip" width="246" height="142" viewBox="0 0 246 142" aria-label="Smart chip">
    <polygon points="0,0 246,0 246,142 67,142 0,76" fill="var(--chip-grey)"/>
  </svg>

  <div class="magnetic-stripe"></div>

  <p class="brand-name brand-bottom"><span>BRIGHT</span><span class="line-two">LEDGER CO</span></p>

  <div class="rule"></div>
</div>
</body>
</html>
```